Iron Ridge Roofing Business Card

Need a business card with the logo that was designed here

Contact Information for Business Card

Name, Title, Phone, Email, Website, Company name

```html
<!DOCTYPE html>
<html lang="en">
<head>
<meta charset="utf-8">
<title>Iron Ridge Roofing – Business Card</title>
<link href="https://fonts.googleapis.com/css2?family=Montserrat:wght@400;600&display=swap" rel="stylesheet">
<style>
  :root {
    --page-bg: #d9d6d1;
    --card-bg: #eceef0;
    --band-blue: #2f6cc0;
    --band-blue-deep: #1f4c86;
    --band-line: #f3f1ec;
    --text-light: #f2f0ea;
    --text-gray: #666a6e;
    --icon-blue: #2a5aa3;
    --brand-blue: #23529a;
  }
  html, body {
    margin: 0;
    width: 1200px;
    height: 897px;
    overflow: hidden;
    background: var(--page-bg);
    font-family: "Montserrat", sans-serif;
  }
  .card {
    position: absolute;
    left: 80px;
    top: 165px;
    width: 1040px;
    height: 568px;
    border-radius: 26px;
    background: var(--card-bg);
    overflow: hidden;
    box-shadow: 0 10px 30px rgba(0,0,0,0.15);
  }
  .header-band {
    position: absolute;
    left: 0; top: 0;
    width: 100%;
    height: 190px;
    background: linear-gradient(100deg, var(--band-blue-deep) 0%, var(--band-blue) 40%, var(--band-blue-deep) 100%);
  }
  .header-strip {
    position: absolute;
    left: 0; top: 196px;
    width: 100%;
    height: 24px;
    background: linear-gradient(100deg, var(--band-blue-deep) 0%, var(--band-blue) 40%, var(--band-blue-deep) 100%);
  }
  .person-name {
    position: absolute;
    left: 55px; top: 58px;
    margin: 0;
    font-size: 34px;
    font-weight: 600;
    letter-spacing: 1.5px;
    color: var(--text-light);
  }
  .person-title {
    position: absolute;
    left: 53px; top: 102px;
    margin: 0;
    font-size: 22px;
    font-weight: 400;
    letter-spacing: 1px;
    color: var(--text-light);
  }
  .address {
    position: absolute;
    left: 55px; top: 290px;
    margin: 0;
    font-style: normal;
    font-size: 22px;
    line-height: 33px;
    letter-spacing: 1px;
    color: var(--text-gray);
  }
  .contact-list {
    position: absolute;
    left: 55px; top: 400px;
    margin: 0; padding: 0;
    list-style: none;
    font-size: 22px;
    letter-spacing: 1px;
    color: var(--text-gray);
  }
  .contact-list li {
    display: flex;
    align-items: center;
    height: 39px;
  }
  .contact-list svg {
    width: 18px; height: 18px;
    margin-right: 10px;
    fill: var(--icon-blue);
  }
  .brand {
    position: absolute;
    left: 600px; top: 370px;
    display: flex;
    align-items: center;
    gap: 14px;
    font-size: 34px;
    font-weight: 600;
    letter-spacing: 1px;
    color: var(--brand-blue);
  }
  .brand-square {
    width: 26px; height: 26px;
    background: var(--brand-blue);
  }
</style>
</head>
<body>
  <div class="card">
    <div class="header-band"></div>
    <div class="header-strip"></div>

    <h1 class="person-name">DERMOT CALLOWAY</h1>
    <p class="person-title">Managing Director</p>

    <address class="address">1480 W Harlan Street<br>Maple County Name 4187</address>

    <ul class="contact-list">
      <li>
        <svg viewBox="0 0 24 24" aria-hidden="true"><path d="M6.6 10.8a15 15 0 0 0 6.6 6.6l2.2-2.2a1 1 0 0 1 1-.25 11.4 11.4 0 0 0 3.6.57 1 1 0 0 1 1 1V20a1 1 0 0 1-1 1A17 17 0 0 1 3 4a1 1 0 0 1 1-1h3.5a1 1 0 0 1 1 1c0 1.25.2 2.45.57 3.57a1 1 0 0 1-.25 1z"/></svg>
        0412 587 263
      </li>
      <li>
        <svg viewBox="0 0 24 24" aria-hidden="true"><path d="M3 5h18a1 1 0 0 1 1 1v12a1 1 0 0 1-1 1H3a1 1 0 0 1-1-1V6a1 1 0 0 1 1-1zm1 2.2V17h16V7.2l-8 5.3z"/></svg>
        info@ironridgeroofing.com
      </li>
      <li>
        <svg viewBox="0 0 24 24" aria-hidden="true"><path d="M12 2a10 10 0 1 0 0 20 10 10 0 0 0 0-20zm6.9 9h-3a15 15 0 0 0-1.3-5.6A8 8 0 0 1 18.9 11zM12 4.1c.9 1.2 1.7 3.6 1.9 6.9h-3.8c.2-3.3 1-5.7 1.9-6.9zM9.4 5.4A15 15 0 0 0 8.1 11h-3a8 8 0 0 1 4.3-5.6zM5.1 13h3a15 15 0 0 0 1.3 5.6A8 8 0 0 1 5.1 13zm6.9 6.9c-.9-1.2-1.7-3.6-1.9-6.9h3.8c-.2 3.3-1 5.7-1.9 6.9zm2.6-1.3a15 15 0 0 0 1.3-5.6h3a8 8 0 0 1-4.3 5.6z"/></svg>
        www.ironridgeroofing.com
      </li>
    </ul>

    <div class="brand">
      <span class="brand-square"></span>
      <span class="brand-name">Iron Ridge Roofing</span>
    </div>
  </div>
</body>
</html>
```